Velmiro Partners Logo and Business Card Design

We already have the rough logo shape (however please make the lines on the logo much thicker so a dark background is not required to see it) . see photos uploaded.
It needs to be refined with color and digitized and then have a front and back business card layout done.
The services are high vibration healing support through a therapy and feng shui service offering. We want people to Feel Happiness, Feel Prosperity and Feel Peace. (the back of the card would have these phrases on it) So a warm, calm and peaceful feeling card.
We would like the card to use the logo provided (with thicker lines and color added) but below the graphic please use the name "Velmiro Partners" NOT Velmiro.
We also would like to use the colors in the colorized matrix shown in photos (gold and purple) but on the lighter side. Thanks for your time!

Front of Card should include: Logo, with Company Name: Velmiro Partners as part of logo, Name: Dara Kovic email: dara@velmiro.example web: www.velmiro.example mobile: 555.018.2946 at bottom of front list Family Constellation | Feng Shui

Back of Card should have the logo and the following listed vertically:

PERSONAL | BUSINESS (Larger size then smaller bullet items below)
*Find Happiness
*Find Prosperity
*Find Peace

Target Market(s)

Target market is both business and personal

Contact Information for Business Card

Front of Card should include: Logo, with Company Name: Velmiro Partners as part of logo, Name: Dara Kovic email: dara@velmiro.example web: www.velmiro.example mobile: 555.018.2946 at bottom of front list Family Constellation | Feng Shui ++++ Back of Card should have the logo and the following listed vertically: PERSONAL | BUSINESS (Larger size then smaller bullet items below) *Find Happiness *Find Prosperity *Find Peace

Font styles to use
Sans Serif

Colors

Designer to choose colors to be used in the design.

Requirements
Nice to have
• Nice light contrast color for the back of card background
Should not have
• No dark colored background on Card.

```html
<!DOCTYPE html>
<html lang="en">
<head>
<meta charset="utf-8">
<title>Velmiro Partners Business Card</title>
<link rel="stylesheet" href="https://fonts.googleapis.com/css2?family=Montserrat:wght@500;600&family=Arimo:wght@400&display=swap">
<style>
  :root {
    --backdrop: #e9e9e9;
    --card: #fbf7ee;
    --card-back: #f3eef9;
    --gold: #c99a34;
    --gold-deep: #b8862a;
    --purple: #9577cf;
    --text: #3d3a36;
    --rule: #d8c9a4;
  }
  * { margin: 0; padding: 0; box-sizing: border-box; }
  html, body {
    width: 1200px; height: 802px; overflow: hidden;
    background: var(--backdrop);
  }
  .stage {
    position: relative; width: 1200px; height: 802px;
    display: flex; align-items: center; justify-content: center; gap: 60px;
  }
  .card {
    position: relative; width: 520px; height: 297px;
    border-radius: 3px;
    box-shadow: 0 10px 24px rgba(0,0,0,.14);
  }
  .card--front { background: var(--card); }
  .card--back {
    background: var(--card-back);
    display: flex; flex-direction: column; align-items: center; justify-content: center;
  }

  .brand {
    position: absolute; right: 34px; top: 62px;
    display: flex; align-items: center; gap: 12px;
  }
  .brand__mark {
    width: 34px; height: 34px; border-radius: 50%;
    border: 3px solid var(--purple);
  }
  .brand__name {
    font-family: "Montserrat", sans-serif; font-weight: 600;
    font-size: 17px; letter-spacing: 1.5px; color: var(--gold);
    text-transform: uppercase;
  }
  .holder {
    position: absolute; left: 34px; top: 140px;
    font-family: "Montserrat", sans-serif; font-weight: 600;
    font-size: 21px; letter-spacing: .5px; color: var(--gold-deep);
    text-transform: uppercase;
  }
  .divider {
    position: absolute; left: 34px; right: 34px; top: 170px;
    height: 1px; background: var(--rule);
  }
  .contacts {
    position: absolute; left: 34px; top: 182px;
    list-style: none;
    font-family: "Arimo", sans-serif; font-size: 15px; color: var(--text);
  }
  .contacts li { display: flex; align-items: center; gap: 9px; height: 24px; }
  .contacts svg { width: 14px; height: 14px; flex: none; }
  .services {
    position: absolute; right: 60px; top: 182px;
    list-style: none;
    font-family: "Arimo", sans-serif; font-size: 15px; color: var(--text);
  }
  .services li { display: flex; align-items: center; gap: 7px; height: 22px; }
  .services li::before {
    content: ""; width: 5px; height: 5px; border-radius: 50%; background: var(--gold);
  }

  .back-mark {
    width: 52px; height: 52px; border-radius: 50%;
    border: 5px solid var(--purple);
  }
  .back-name {
    margin-top: 10px;
    font-family: "Montserrat", sans-serif; font-weight: 600;
    font-size: 17px; letter-spacing: 2px; color: var(--gold);
    text-transform: uppercase;
  }
  .back-audience {
    margin-top: 18px;
    font-family: "Montserrat", sans-serif; font-weight: 600;
    font-size: 15px; letter-spacing: 1.5px; color: var(--purple);
    text-transform: uppercase;
  }
  .back-list {
    margin-top: 8px; list-style: none;
    font-family: "Arimo", sans-serif; font-size: 13px; color: var(--text);
  }
  .back-list li { display: flex; align-items: center; gap: 7px; height: 20px; }
  .back-list li::before {
    content: ""; width: 5px; height: 5px; border-radius: 50%; background: var(--gold);
  }
</style>
</head>
<body>
<main class="stage">
  <section class="card card--front" aria-label="Card front">
    <div class="brand">
      <span class="brand__mark"></span>
      <span class="brand__name">Velmiro Partners</span>
    </div>
    <p class="holder">Dara Kovic</p>
    <div class="divider"></div>
    <ul class="contacts">
      <li>
        <svg viewBox="0 0 14 14" aria-hidden="true"><circle cx="7" cy="7" r="7" fill="var(--gold)"/><path d="M4.3 3.6l1.5-.3.7 1.8-.9.7c.5 1 1.2 1.7 2.2 2.2l.7-.9 1.8.7-.3 1.5c-3.3 0-5.7-2.4-5.7-5.7z" fill="var(--card)"/></svg>
        555.018.2946
      </li>
      <li>
        <svg viewBox="0 0 14 14" aria-hidden="true"><rect x="1" y="3" width="12" height="8" rx="1" fill="var(--gold)"/><path d="M1.5 3.5L7 8l5.5-4.5" fill="none" stroke="var(--card)" stroke-width="1"/></svg>
        dara@velmiro.example
      </li>
      <li>
        <svg viewBox="0 0 14 14" aria-hidden="true"><circle cx="7" cy="7" r="6.5" fill="var(--gold)"/><g fill="none" stroke="var(--card)" stroke-width=".9"><circle cx="7" cy="7" r="4"/><ellipse cx="7" cy="7" rx="1.8" ry="4"/><path d="M3 7h8"/></g></svg>
        www.velmiro.example
      </li>
    </ul>
    <ul class="services">
      <li>Family Constellation</li>
      <li>Feng Shui</li>
    </ul>
  </section>

  <section class="card card--back" aria-label="Card back">
    <span class="back-mark"></span>
    <span class="back-name">Velmiro Partners</span>
    <p class="back-audience">Personal | Business</p>
    <ul class="back-list">
      <li>Find Happiness</li>
      <li>Find Prosperity</li>
      <li>Find Peace</li>
    </ul>
  </section>
</main>
</body>
</html>
```